Fahrzeugbeschriftung für ambulanten Pflegedienst
Zielgruppe
Ambulanter Pflegedienst
(Bitte um deutsche Kommunikation)
Aufgabenstellung
Unser Logo und unser Motto, farbliche Komponenten, die wichtigste Leistungen, Mail Adresse, Flyer vorhanden, Fahrzeuge haben einen weißen Hintergrund. Es sind 3 Fahrzeug Modelle : Zipo Kleinflink Baujahr 2008, Norvak Reihe 5 Baujahr 2023 und KR Ilo 2 Türig Baujahr 2008, Kontaktdaten wie Telefonnummer und Mail Adresse müssen sichtlich sein.
Die Welle im Flyer soll auch auf den Fahrzeugen abgebildet sein.
Hierbei stellen wir uns folgendes vor:
Die zweifarbige Teilung, mit der Welle, soll sich von A - Säule bis C-Säule vollstrecken.
Abbildungen vom Flyer soll genutzt werden, z.B. Die Hand mit den Personen.
Ein Beispiel, für Auffälligkeit habe ich 3 Bilder von anderen Fahrzeugen beigefügt (nur als Beispiel)
Die Schrift 'Ambulanter Pflegedienst' muss betont sein.
Zu unseren Leistungen die aufgeführt werden müssen;
- Grundpflege
- Behandlungspflege
- Wundmanagement
- Pflegeberatung

```html
<!DOCTYPE html>
<html lang="de">
<head>
<meta charset="utf-8">
<title>Fahrzeugbeschriftung – Pflegehafen Ambulanter Pflegedienst</title>
<link rel="stylesheet" href="https://fonts.googleapis.com/css2?family=Poppins:wght@500;700;800&display=swap">
<style>
  :root {
    --page: #ffffff;
    --panel-light: #e8e9ec;
    --blue: #0aa6de;
    --cyan: #14b4d4;
    --ink: #1b1b1f;
    --white: #ffffff;
    --skin-light: #f3d9c8;
    --skin-mid: #e7b9a0;
  }
  * { box-sizing: border-box; margin: 0; padding: 0; }
  html, body {
    width: 1200px; height: 1200px; overflow: hidden;
    background: var(--page);
    font-family: "Poppins", Arial, sans-serif;
  }
  .wrap-panel {
    position: absolute; left: 60px; top: 360px;
    width: 1080px; height: 480px;
    border-radius: 28px; overflow: hidden;
    background: var(--panel-light);
  }
  .wrap-art { position: absolute; inset: 0; width: 100%; height: 100%; }
  .brand {
    position: absolute; left: 40px; top: 150px;
    color: var(--white);
    display: flex; align-items: center; gap: 8px;
  }
  .brand-dot { width: 16px; height: 16px; border-radius: 50%; background: var(--white); }
  .brand-name { font-weight: 700; font-size: 21px; line-height: 1; }
  .brand-tagline {
    position: absolute; left: 64px; top: 178px;
    color: var(--white); font-size: 9px; font-weight: 500;
  }
  .message {
    position: absolute; left: 300px; top: 50px;
    transform: rotate(-4deg); transform-origin: left top;
    color: var(--ink);
  }
  .headline {
    font-weight: 800; font-size: 40px; line-height: 1.15; letter-spacing: 1px;
  }
  .services { list-style: none; margin-top: 20px; }
  .services li {
    position: relative; padding-left: 40px;
    font-weight: 700; font-size: 17px; line-height: 24px; letter-spacing: 1px;
  }
  .services li::before {
    content: ""; position: absolute; left: 0; top: 7px;
    width: 11px; height: 11px; border-radius: 50%; background: var(--ink);
  }
  .contact {
    position: absolute; left: 310px; top: 405px;
    transform: rotate(-4deg); transform-origin: left top;
    display: flex; align-items: center; gap: 16px;
    color: var(--white); font-weight: 700; font-size: 24px; letter-spacing: 1.5px;
  }
  .contact-icon {
    width: 30px; height: 30px; border-radius: 50%; background: var(--white);
    display: flex; align-items: center; justify-content: center;
  }
</style>
</head>
<body>
  <section class="wrap-panel">
    <svg class="wrap-art" viewBox="0 0 1080 480" preserveAspectRatio="none">
      <defs>
        <linearGradient id="skin" x1="0" y1="0" x2="1" y2="1">
          <stop offset="0" stop-color="var(--skin-light)"/>
          <stop offset="1" stop-color="var(--skin-mid)"/>
        </linearGradient>
        <linearGradient id="base-blue" x1="0" y1="0" x2="1" y2="0">
          <stop offset="0" stop-color="var(--cyan)"/>
          <stop offset="1" stop-color="var(--blue)"/>
        </linearGradient>
      </defs>
      <rect x="520" y="0" width="560" height="300" fill="url(#skin)" role="img" aria-label="Foto: ineinander gelegte Hände als Zeichen von Fürsorge"/>
      <path d="M0,80 C200,60 330,200 440,290 C560,370 800,300 1080,220 L1080,480 L0,480 Z" fill="url(#base-blue)"/>
    </svg>

    <div class="brand"><span class="brand-dot"></span><span class="brand-name">Pflegehafen</span></div>
    <div class="brand-tagline">Ambulanter Pflegedienst</div>

    <div class="message">
      <h1 class="headline">Ambulanter<br>Pflegedienst</h1>
      <ul class="services">
        <li>Grundpflege</li>
        <li>Behandlungspflege</li>
        <li>Wundmanagement</li>
        <li>Pflegeberatung § 37.3</li>
      </ul>
    </div>

    <div class="contact">
      <span class="contact-icon">
        <svg width="16" height="12" viewBox="0 0 16 12"><rect x="0" y="0" width="16" height="12" rx="1.5" fill="var(--blue)"/><path d="M1,1.5 L8,7 L15,1.5" stroke="var(--white)" stroke-width="1.6" fill="none"/></svg>
      </span>
      <span class="contact-mail">info@pflegehafen-dienst.de</span>
    </div>
  </section>
</body>
</html>
```